Metal Fabrication Business Cards

We need a business card for our business of Metal Fabrication/Welding. Our company is called "Hadley's Metal Fabrication"

We are a metal fabrication business which takes on "high class" clients- dealing with some of the biggest builders in Australia. Our work is neat, and the type of work we do is 2nd to none for quality. We want to show that on our cards. However, we would love to show a side that is down to earth and a bit more modern and contemporary - we are all young in business so would love to show that side - rather than a boring "very straight looking" card. We always have a clean workshop and take pride in our presentation. We want to come across like we are very rich, but would love to go for a surf as well! A card that basically says we have high class and will charge you a high rate - but the quality will be outstanding.

Front of card: - Simply but sharp!
-Thinking maybe white card - with nice black writing.
-On the right hand side of card a person welding - or holding a welder.
- My business name - Hadley's Metal Fabrication
-Also maybe my name - which is 'Corey" (if it doesn't work, we can put this on the back of card.)
- if needed to look better - we can put keywords on front of card like "metal fabrication, sheet metal, welding etc" but I dont want it to be crowded.

Back of card: - Also make smart but sharp!
Put details such as:
04376 81 302
hadley.fabrication@mailbox-ink.com
7/23 Heron Street
East Ridgeway QLD 4571
www.ridgewayfabrication.com.au
ABN 71 530 864 217

thats just an idea - its now up to you. I don't mind what you come up with - as long as it stands out from the rest and looks sharp, professional but contemporary.

Business

Put details such as:
04376 81 302
7/23 Heron Street
East Ridgeway QLD 4571
ABN 71 530 864 217

Hadley's Metal Fabrication

```html
<!DOCTYPE html>
<html lang="en">
<head>
<meta charset="utf-8">
<title>Hadley's Metal Fabrication – Business Card</title>
<link href="https://fonts.googleapis.com/css2?family=Roboto+Condensed:wght@400;700&display=swap" rel="stylesheet">
<style>
  :root {
    --backdrop: #eceeee;
    --card-white: #ffffff;
    --card-dark: #2b2a29;
    --ink: #2b2a29;
    --text-light: #f4f4f4;
    --accent-orange: #f7941d;
    --stripe-red: #e5252a;
    --stripe-orange: #f7941d;
    --stripe-yellow: #ffd400;
  }
  * { box-sizing: border-box; margin: 0; padding: 0; }
  html, body {
    width: 1200px;
    height: 873px;
    overflow: hidden;
    background: var(--backdrop);
  }
  .card {
    position: absolute;
    left: 149px;
    top: 183px;
    width: 870px;
    height: 524px;
    border-radius: 40px;
    overflow: hidden;
    background: var(--card-dark);
    font-family: "Roboto Condensed", sans-serif;
  }
  .card__top {
    position: absolute;
    left: 0; top: 0;
    width: 100%;
    height: 224px;
    background: var(--card-white);
  }
  .card__stripe {
    position: absolute;
    left: 0; top: 224px;
    width: 100%;
    height: 10px;
    background: linear-gradient(90deg, var(--stripe-red) 0%, var(--stripe-orange) 25%, var(--stripe-yellow) 50%, var(--stripe-orange) 75%, var(--stripe-red) 100%);
  }
  .card__gap {
    position: absolute;
    left: 0; top: 234px;
    width: 100%;
    height: 3px;
    background: var(--card-white);
  }
  .brand {
    position: absolute;
    left: 249px;
    top: 112px;
    color: var(--ink);
    font-weight: 700;
    font-size: 34px;
    line-height: 46px;
  }
  .brand__name { display: block; text-transform: uppercase; }
  .brand__trade { display: block; }
  .abn {
    position: absolute;
    left: 57px;
    top: 270px;
    color: var(--accent-orange);
    font-size: 26px;
    line-height: 32px;
    font-weight: 400;
  }
  .contacts {
    position: absolute;
    left: 320px;
    top: 262px;
    list-style: none;
    color: var(--text-light);
    font-size: 26px;
    line-height: 32px;
  }
  .contacts__item {
    position: relative;
    padding-left: 48px;
    margin-bottom: 20px;
  }
  .contacts__item--address { line-height: 31px; padding-top: 2px; }
  .contacts__icon {
    position: absolute;
    left: 0;
    top: 2px;
    width: 30px;
    height: 30px;
  }
  .contacts__icon--pin { top: 4px; height: 38px; }
</style>
</head>
<body>
  <div class="card">
    <div class="card__top"></div>
    <div class="card__stripe"></div>
    <div class="card__gap"></div>

    <div class="brand">
      <span class="brand__name">Hadley's</span>
      <span class="brand__trade">Metal Fabrication</span>
    </div>

    <p class="abn">ABN 71 530 864 217</p>

    <ul class="contacts">
      <li class="contacts__item">
        <svg class="contacts__icon" viewBox="0 0 30 30" aria-hidden="true">
          <g fill="none" stroke="#f7941d" stroke-width="2">
            <circle cx="15" cy="15" r="12"/>
            <ellipse cx="15" cy="15" rx="5" ry="12"/>
            <line x1="3" y1="15" x2="27" y2="15"/>
            <line x1="15" y1="3" x2="15" y2="27"/>
          </g>
        </svg>
        www.ridgewayfabrication.com.au
      </li>
      <li class="contacts__item">
        <svg class="contacts__icon" viewBox="0 0 30 30" aria-hidden="true">
          <rect x="7" y="1" width="17" height="28" rx="3" fill="none" stroke="#f7941d" stroke-width="2.2"/>
          <rect x="10" y="5" width="11" height="17" fill="none" stroke="#f7941d" stroke-width="1.5"/>
          <circle cx="15.5" cy="25.5" r="1.4" fill="#f7941d"/>
        </svg>
        04376 81 302
      </li>
      <li class="contacts__item">
        <svg class="contacts__icon" viewBox="0 0 30 30" aria-hidden="true">
          <rect x="1" y="7" width="28" height="18" fill="none" stroke="#f7941d" stroke-width="2"/>
          <polyline points="1,7 15,18 29,7" fill="none" stroke="#f7941d" stroke-width="2"/>
          <line x1="1" y1="25" x2="11" y2="15" stroke="#f7941d" stroke-width="2"/>
          <line x1="29" y1="25" x2="19" y2="15" stroke="#f7941d" stroke-width="2"/>
        </svg>
        hadley.fabrication@mailbox-ink.com
      </li>
      <li class="contacts__item contacts__item--address">
        <svg class="contacts__icon contacts__icon--pin" viewBox="0 0 30 38" aria-hidden="true">
          <path d="M15 1 C7 1 2 7 2 14 C2 23 15 37 15 37 C15 37 28 23 28 14 C28 7 23 1 15 1 Z" fill="#f7941d"/>
          <circle cx="15" cy="14" r="5" fill="#2b2a29"/>
        </svg>
        7/23 Heron Street<br>East Ridgeway QLD 4571
      </li>
    </ul>
  </div>
</body>
</html>
```